Expense Tracker App for Young Adults

I need a mobile app designer to design an app UI for me. It is for an expense tracker app. I’ve attached a mind map of the various screens and features of the app.

I would like to see designs for this app which is targeted towards young adults (late teens & early 20s) just starting their career who want to plan their budgets and track their expenses.
Updates

Hello designers! I'm conscious that this is not a guaranteed project, so I can understand that some of you might be apprehensive. Just wanted to let you know that I'm willing to see your initial drafts that show your direction and theme for design. You don't have to design the whole app. In fact, it's better if you share your initial design ideas so that we can have a discussion and I can give my input. If I see some good initial designs, I will be happy to make this a guaranteed project. I'm simply being cautious since I'm bootstrapping this and funding out of my own pocket. Thank you for your understanding!

Target Market(s)

Young adults who are just starting their careers, late teens and early 20s.

Font styles to use
Sans Serif

Requirements
Must have
• Ease of use, smart and sleek, a guided setup wizard which will help users setup their account after signing up.
Should not have
• Clunky

```html
<!DOCTYPE html>
<html lang="en">
<head>
<meta charset="utf-8">
<title>Expense Tracker – App Design</title>
<link href="https://fonts.googleapis.com/css2?family=Montserrat:wght@800&family=Source+Sans+3:wght@400;600;700&display=swap" rel="stylesheet">
<style>
:root{
  --stage:#1b1a1f;
  --purple:#9444de;
  --purple-soft:#b57cf0;
  --plum-dark:#2e1540;
  --plum:#55277a;
  --ink:#1d1b22;
  --muted:#6f6d78;
  --line:#e3e1e8;
  --surface:#ffffff;
  --page:#f7f6f9;
  --red:#e5404a;
  --teal:#27bcd9;
  --green:#45ad4f;
  --yellow:#f4c72a;
  --lilac:#a972e6;
}
*{box-sizing:border-box;margin:0;padding:0}
html,body{width:1200px;height:960px;overflow:hidden}
body{background:var(--stage);font-family:"Source Sans 3",sans-serif;color:var(--ink);position:relative}
.hero{position:absolute;top:52px;left:0;width:1200px;text-align:center;font-family:"Montserrat",sans-serif;font-weight:800}
.hero-title{font-size:40px;color:var(--purple);letter-spacing:.5px}
.hero-sub{font-size:32px;color:transparent;-webkit-text-stroke:1.5px var(--purple);margin-top:4px}

.screen{position:absolute;top:210px;width:296px;height:640px;border-radius:34px;overflow:hidden;background:var(--surface)}
.screen-login{left:116px}
.screen-home{left:452px;background:var(--page)}
.screen-report{left:788px;background:var(--page)}
.abs{position:absolute}
.status{position:absolute;top:14px;left:22px;right:20px;display:flex;justify-content:space-between;font-size:13px;font-weight:600}
.status-light{color:#fff}
.status svg{display:block}
.home-bar{position:absolute;bottom:8px;left:50%;width:100px;height:4px;border-radius:2px;transform:translateX(-50%);background:var(--ink)}

/* login */
.brand{top:150px;left:0;width:100%;display:flex;align-items:center;justify-content:center;gap:8px}
.brand-dot{width:22px;height:22px;border-radius:50%;background:var(--purple)}
.brand-name{font-size:24px;font-weight:600;color:var(--plum)}
.login-title{top:280px;left:18px;font-size:20px;font-weight:700}
.field-card{top:318px;left:16px;right:16px;height:118px;border-radius:8px;background:#fff;box-shadow:0 4px 16px rgba(40,20,60,.12)}
.field{position:absolute;left:14px;right:14px;display:flex;align-items:center;gap:12px;font-size:13px;color:var(--muted)}
.field-user{top:20px;padding-bottom:14px;border-bottom:1px solid var(--line)}
.field-pass{top:76px}
.forgot{top:476px;left:18px;font-size:12px;font-weight:600;color:var(--purple)}
.btn-login{top:464px;right:18px;width:94px;height:40px;border-radius:20px;background:linear-gradient(90deg,var(--purple),#a85ae8);color:#fff;font-size:13px;font-weight:700;display:flex;align-items:center;justify-content:center}
.signup-band{bottom:0;left:0;right:0;height:82px;background:linear-gradient(180deg,#3d1c55,var(--plum-dark))}
.signup-text{position:absolute;left:16px;top:30px;color:#fff;font-size:13px}
.btn-signup{position:absolute;right:16px;top:22px;width:74px;height:32px;border:1.5px solid #fff;border-radius:16px;color:#fff;font-size:12px;font-weight:700;display:flex;align-items:center;justify-content:center}
.signup-band .home-bar{background:#fff}

/* shared header */
.header{top:0;left:0;right:0;background:linear-gradient(180deg,var(--plum-dark),var(--plum));border-radius:0 0 14px 14px}
.header-home{height:186px}
.avatar{top:50px;left:16px;width:40px;height:40px;border-radius:50%;background:linear-gradient(135deg,#4f8fd8,#c98d6e)}
.greet-small{top:54px;left:68px;font-size:10px;color:#d8c9e6;letter-spacing:.5px}
.greet-name{top:66px;left:68px;font-size:19px;font-weight:700;color:#fff}
.icon-bell{top:58px;left:226px}
.badge{top:51px;left:238px;width:15px;height:15px;border-radius:50%;background:var(--red);color:#fff;font-size:9px;font-weight:700;display:flex;align-items:center;justify-content:center}
.icon-filter{top:60px;left:258px}
.balance-card{top:103px;left:9px;right:9px;height:92px;background:#fff;border-radius:10px;overflow:hidden;box-shadow:0 6px 18px rgba(40,20,60,.15)}
.balance-label{position:absolute;top:20px;left:18px;font-size:11px;color:var(--muted);letter-spacing:.4px}
.balance-value{position:absolute;top:40px;left:18px;font-size:24px;font-weight:700}
.ring-outer{position:absolute;right:-30px;top:-30px;width:110px;height:110px;border-radius:50%;background:#f1e6fb}
.ring-mid{position:absolute;right:-14px;top:-14px;width:80px;height:80px;border-radius:50%;background:#d9b9f5}
.ring-core{position:absolute;right:0;top:0;width:52px;height:52px;border-radius:50%;background:var(--purple);display:flex;align-items:center;justify-content:center}

.tabs{top:212px;left:18px;right:18px;display:flex;justify-content:space-between;font-size:13px}
.tab-active{color:var(--purple);font-weight:600;position:relative}
.tab-active::after{content:"";position:absolute;left:0;right:0;bottom:-7px;height:2px;background:var(--purple)}

.day-card{left:17px;right:17px;background:#fff;border-radius:8px;box-shadow:0 2px 10px rgba(40,20,60,.07);overflow:hidden}
.day-head{position:relative;height:56px;border-bottom:2px dotted #c9c6d2;margin:0 6px}
.day-num{position:absolute;left:0;top:12px;width:48px;height:30px;border-radius:0 15px 15px 0;background:#f0eef3;font-size:15px;font-weight:600;display:flex;align-items:center;justify-content:center;margin-left:-6px}
.day-tag{position:absolute;left:58px;top:14px;font-size:8px;color:var(--muted);letter-spacing:.4px}
.day-month{position:absolute;left:58px;top:25px;font-size:11px}
.day-total{position:absolute;right:6px;top:20px;font-size:14px;font-weight:700;color:var(--red)}
.tx{position:relative;height:52px}
.tx-icon{position:absolute;left:12px;top:10px;width:32px;height:32px;border-radius:50%;display:flex;align-items:center;justify-content:center}
.tx-name{position:absolute;left:58px;top:10px;font-size:13px}
.tx-note{position:absolute;left:58px;top:28px;font-size:9px;color:var(--muted)}
.tx-amt{position:absolute;right:12px;top:16px;font-size:12px;color:var(--red)}
.bg-teal{background:var(--teal)}
.bg-yellow{background:var(--yellow)}
.bg-green{background:var(--green)}
.bg-lilac{background:var(--lilac)}

.nav{bottom:0;left:0;right:0;height:58px;background:#fff;border-top:1px solid var(--line);display:flex;justify-content:space-around;align-items:center;padding:0 10px 12px}
.nav-slot{width:26px;display:flex;justify-content:center;position:relative}
.nav-slot.active::before{content:"";position:absolute;top:-10px;width:26px;height:2px;background:var(--purple)}
.fab{width:36px;height:36px;border-radius:50%;background:var(--purple);margin-top:-30px;display:flex;align-items:center;justify-content:center;box-shadow:0 4px 10px rgba(148,68,222,.45)}

/* report */
.header-report{height:228px}
.view-small{top:44px;left:14px;font-size:9px;color:#d8c9e6;letter-spacing:.5px}
.view-range{top:56px;left:14px;font-size:15px;font-weight:700;color:#fff}
.icon-cal{top:60px;right:14px}
.chip{top:92px;height:28px;border-radius:6px;display:flex;align-items:center;gap:5px;padding:0 8px;font-size:9px;color:#fff}
.chip-on{left:12px;width:124px;background:var(--purple)}
.chip-off{left:144px;width:140px;background:#6d4b84}
.split-card{top:136px;left:9px;right:9px;height:72px;background:#fff;border-radius:8px;display:flex;box-shadow:0 6px 18px rgba(40,20,60,.15)}
.split-col{flex:1;padding:16px 0 0 22px}
.split-col+.split-col{border-left:1px solid var(--line)}
.split-label{font-size:8px;color:var(--muted);letter-spacing:.3px}
.split-value{font-size:14px;font-weight:700;margin-top:4px}
.exp-title{top:236px;left:14px;font-size:14px;font-weight:600}
.exp-total{top:238px;right:14px;font-size:12px;font-weight:600;color:var(--red)}
.donut{top:262px;left:0;width:296px;height:150px}
.cat-label{top:420px;left:14px;font-size:9px;color:var(--muted);letter-spacing:.4px}
.cat-card{width:126px;height:52px;background:#fff;border-radius:6px;box-shadow:0 2px 8px rgba(40,20,60,.08)}
.cat-icon{position:absolute;left:8px;top:8px;width:18px;height:18px;border-radius:50%;display:flex;align-items:center;justify-content:center}
.cat-amt{position:absolute;right:8px;top:10px;font-size:11px;color:var(--red)}
.cat-name{position:absolute;left:8px;top:32px;font-size:10px}
</style>
</head>
<body>

<header class="hero">
  <div class="hero-title">Expense Tracker</div>
  <div class="hero-sub">App Design</div>
</header>

<!-- Login -->
<section class="screen screen-login">
  <div class="status"><span>9:41</span>
    <svg width="44" height="10" viewBox="0 0 44 10"><rect x="0" y="6" width="2" height="4" fill="#1d1b22"/><rect x="4" y="4" width="2" height="6" fill="#1d1b22"/><rect x="8" y="2" width="2" height="8" fill="#1d1b22"/><path d="M16 4a6 6 0 0 1 8 0M18 6.5a3 3 0 0 1 4 0" stroke="#1d1b22" fill="none" stroke-width="1.3"/><circle cx="20" cy="9" r="1" fill="#1d1b22"/><rect x="28" y="1" width="14" height="8" rx="2" fill="#1d1b22"/></svg>
  </div>
  <div class="abs brand"><span class="brand-dot"></span><span class="brand-name">Pocketwise</span></div>
  <div class="abs login-title">Log in</div>
  <div class="abs field-card">
    <div class="field field-user">
      <svg width="12" height="14" viewBox="0 0 12 14" fill="none" stroke="#3b3a45" stroke-width="1.3"><circle cx="6" cy="4" r="3"/><path d="M1 13c0-3 2.2-5 5-5s5 2 5 5"/></svg>
      username or email</div>
    <div class="field field-pass">
      <svg width="12" height="14" viewBox="0 0 12 14" fill="none" stroke="#3b3a45" stroke-width="1.3"><rect x="1" y="6" width="10" height="7" rx="1"/><path d="M3 6V4a3 3 0 0 1 6 0v2"/></svg>
      password</div>
  </div>
  <div class="abs forgot">FORGOT PASSWORD?</div>
  <div class="abs btn-login">LOG IN</div>
  <div class="abs signup-band">
    <span class="signup-text">Don't have an account?</span>
    <span class="btn-signup">SIGN UP</span>
    <span class="home-bar"></span>
  </div>
</section>

<!-- Home -->
<section class="screen screen-home">
  <div class="abs header header-home"></div>
  <div class="status status-light"><span>9:41</span>
    <svg width="44" height="10" viewBox="0 0 44 10"><rect x="0" y="6" width="2" height="4" fill="#fff"/><rect x="4" y="4" width="2" height="6" fill="#fff"/><rect x="8" y="2" width="2" height="8" fill="#fff"/><path d="M16 4a6 6 0 0 1 8 0M18 6.5a3 3 0 0 1 4 0" stroke="#fff" fill="none" stroke-width="1.3"/><circle cx="20" cy="9" r="1" fill="#fff"/><rect x="28" y="1" width="14" height="8" rx="2" fill="#fff"/></svg>
  </div>
  <div class="abs avatar" role="img" aria-label="Profile photo of the user"></div>
  <div class="abs greet-small">GOOD MORNING</div>
  <div class="abs greet-name">Marco</div>
  <svg class="abs icon-bell" width="18" height="20" viewBox="0 0 18 20" fill="none" stroke="#fff" stroke-width="1.6"><path d="M3 14V9a6 6 0 0 1 12 0v5l2 2H1z"/><path d="M7 18h4"/></svg>
  <div class="abs badge">8</div>
  <svg class="abs icon-filter" width="18" height="18" viewBox="0 0 18 18" fill="none" stroke="#fff" stroke-width="1.6"><path d="M1 2h16l-6 7v7l-4-2V9z"/></svg>

  <div class="abs balance-card">
    <div class="ring-outer"></div><div class="ring-mid"></div>
    <div class="ring-core"><svg width="22" height="20" viewBox="0 0 22 20" fill="#fff"><circle cx="7" cy="12" r="6"/><rect x="15" y="6" width="7" height="2"/><rect x="15" y="10" width="7" height="2"/><rect x="15" y="14" width="7" height="2"/></svg></div>
    <div class="balance-label">CURRENT BALANCE</div>
    <div class="balance-value">$1,450.00</div>
  </div>

  <div class="abs tabs"><span>Last Month</span><span class="tab-active">This Month</span><span>Future</span></div>

  <div class="abs day-card" style="top:245px">
    <div class="day-head"><span class="day-num">18</span><span class="day-tag">TODAY</span><span class="day-month">September 2020</span><span class="day-total">-120.00</span></div>
    <div class="tx" style="margin-top:6px"><span class="tx-icon bg-teal"><svg width="16" height="14" viewBox="0 0 16 14" fill="none" stroke="#fff" stroke-width="1.5"><path d="M1 4h10v5a4 4 0 0 1-4 4H5a4 4 0 0 1-4-4zM11 5h2a2 2 0 0 1 0 4h-2"/></svg></span><span class="tx-name">Café</span><span class="tx-note">Large coffee &amp; 1 sliced cake</span><span class="tx-amt">-20.00</span></div>
    <div class="tx" style="margin-bottom:6px"><span class="tx-icon bg-yellow"><svg width="14" height="16" viewBox="0 0 14 16" fill="none" stroke="#fff" stroke-width="1.5"><path d="M2 1h10v14l-2-1.5L7 15l-3-1.5L2 15z"/><path d="M5 5h4M5 8h4"/></svg></span><span class="tx-name">Bills</span><span class="tx-note">Internet</span><span class="tx-amt">-100.00</span></div>
  </div>

  <div class="abs day-card" style="top:424px">
    <div class="day-head"><span class="day-num">17</span><span class="day-tag">YESTERDAY</span><span class="day-month">September 2020</span><span class="day-total">-250.00</span></div>
    <div class="tx" style="margin:6px 0"><span class="tx-icon bg-green"><svg width="14" height="14" viewBox="0 0 14 14" fill="none" stroke="#fff" stroke-width="1.5"><rect x="1" y="3" width="12" height="10" rx="1"/><path d="M4 6a3 3 0 0 0 6 0"/></svg></span><span class="tx-name">Shopping</span><span class="tx-note">1 pair of shoes</span><span class="tx-amt">-250.00</span></div>
  </div>

  <div class="abs day-card" style="top:560px;height:60px">
    <div class="day-head" style="border:0"><span class="day-num">16</span><span class="day-tag">WEDNESDAY</span><span class="day-month">September 2020</span><span class="day-total">-80.00</span></div>
  </div>

  <nav class="abs nav">
    <span class="nav-slot active"><svg width="20" height="18" viewBox="0 0 20 18" fill="none" stroke="#9444de" stroke-width="1.6"><rect x="1" y="5" width="16" height="12" rx="2"/><path d="M3 5l9-4 2 4M13 10h5v4h-5z"/></svg></span>
    <span class="nav-slot"><svg width="18" height="18" viewBox="0 0 18 18" fill="none" stroke="#3b3a45" stroke-width="1.6"><path d="M9 1a8 8 0 1 0 8 8H9z"/><path d="M11 1v6h6"/></svg></span>
    <span class="fab"><svg width="14" height="14" viewBox="0 0 14 14" stroke="#fff" stroke-width="2"><path d="M7 1v12M1 7h12"/></svg></span>
    <span class="nav-slot"><svg width="18" height="18" viewBox="0 0 18 18" fill="none" stroke="#3b3a45" stroke-width="1.6"><circle cx="9" cy="9" r="8"/><circle cx="9" cy="9" r="4.5"/><circle cx="9" cy="9" r="1.5"/></svg></span>
    <span class="nav-slot"><svg width="18" height="18" viewBox="0 0 18 18" fill="none" stroke="#3b3a45" stroke-width="1.6"><rect x="1" y="1" width="6" height="6"/><rect x="11" y="1" width="6" height="6"/><rect x="1" y="11" width="6" height="6"/><rect x="11" y="11" width="6" height="6"/></svg></span>
  </nav>
  <span class="home-bar"></span>
</section>

<!-- Report -->
<section class="screen screen-report">
  <div class="abs header header-report"></div>
  <div class="status status-light"><span>9:41</span>
    <svg width="44" height="10" viewBox="0 0 44 10"><rect x="0" y="6" width="2" height="4" fill="#fff"/><rect x="4" y="4" width="2" height="6" fill="#fff"/><rect x="8" y="2" width="2" height="8" fill="#fff"/><path d="M16 4a6 6 0 0 1 8 0M18 6.5a3 3 0 0 1 4 0" stroke="#fff" fill="none" stroke-width="1.3"/><circle cx="20" cy="9" r="1" fill="#fff"/><rect x="28" y="1" width="14" height="8" rx="2" fill="#fff"/></svg>
  </div>
  <div class="abs view-small">VIEW REPORT</div>
  <div class="abs view-range">1 Sep 2020 - 18 Sep 2020</div>
  <svg class="abs icon-cal" width="14" height="15" viewBox="0 0 14 15" fill="none" stroke="#fff" stroke-width="1.4"><rect x="1" y="3" width="12" height="11" rx="1"/><path d="M4 1v3M10 1v3M1 6h12M4 9h1M7 9h1M10 9h1M4 12h1M7 12h1"/></svg>
  <div class="abs chip chip-on"><svg width="12" height="12" viewBox="0 0 12 12" fill="none" stroke="#fff" stroke-width="1.3"><path d="M2 6a4 4 0 1 0 1.2-2.8M1 1v2.5h2.5"/></svg>Historical Expenses</div>
  <div class="abs chip chip-off"><svg width="12" height="12" viewBox="0 0 12 12" fill="none" stroke="#fff" stroke-width="1.3"><path d="M2 10l4-4M4 4l4 4M8 2l2 2"/></svg>Progress Against Goals</div>
  <div class="abs split-card">
    <div class="split-col"><div class="split-label">CURRENT BALANCE</div><div class="split-value">$2,580.00</div></div>
    <div class="split-col"><div class="split-label">ENDING BALANCE</div><div class="split-value">$1,450.00</div></div>
  </div>
  <div class="abs exp-title">Expenses</div>
  <div class="abs exp-total">$1,130.00</div>

  <svg class="abs donut" viewBox="0 0 296 150" font-family="Source Sans 3, sans-serif" font-size="7" fill="#1d1b22">
    <g transform="rotate(-90 148 80)" fill="none" stroke-width="14">
      <circle cx="148" cy="80" r="30" stroke="#f4c72a" stroke-dasharray="9.4 179"/>
      <circle cx="148" cy="80" r="30" stroke="#45ad4f" stroke-dasharray="98 90.5" stroke-dashoffset="-9.4"/>
      <circle cx="148" cy="80" r="30" stroke="#27bcd9" stroke-dasharray="81 107.5" stroke-dashoffset="-107.4"/>
    </g>
    <line x1="154" y1="48" x2="154" y2="26" stroke="#c9c6d2"/>
    <circle cx="154" cy="24" r="7" fill="#f4c72a"/><text x="150" y="10">5%</text>
    <line x1="178" y1="90" x2="208" y2="94" stroke="#c9c6d2"/>
    <circle cx="212" cy="94" r="7" fill="#45ad4f"/><text x="224" y="97">52%</text>
    <line x1="118" y1="72" x2="92" y2="68" stroke="#c9c6d2"/>
    <circle cx="88" cy="68" r="7" fill="#27bcd9"/><text x="64" y="70">43%</text>
  </svg>

  <div class="abs cat-label">CATEGORIES</div>
  <div class="abs cat-card" style="top:438px;left:14px"><span class="cat-icon bg-green"></span><span class="cat-amt">$587.60</span><span class="cat-name">Shopping</span></div>
  <div class="abs cat-card" style="top:438px;left:156px"><span class="cat-icon bg-teal"></span><span class="cat-amt">$485.90</span><span class="cat-name">Foods</span></div>
  <div class="abs cat-card" style="top:500px;left:14px"><span class="cat-icon bg-yellow"></span><span class="cat-amt">$56.50</span><span class="cat-name">Bills &amp; Utilities</span></div>
  <div class="abs cat-card" style="top:500px;left:156px"><span class="cat-icon bg-lilac"></span><span class="cat-amt">$0.00</span><span class="cat-name">Others</span></div>

  <nav class="abs nav">
    <span class="nav-slot"><svg width="20" height="18" viewBox="0 0 20 18" fill="none" stroke="#3b3a45" stroke-width="1.6"><rect x="1" y="5" width="16" height="12" rx="2"/><path d="M3 5l9-4 2 4M13 10h5v4h-5z"/></svg></span>
    <span class="nav-slot active"><svg width="18" height="18" viewBox="0 0 18 18" fill="none" stroke="#9444de" stroke-width="1.6"><path d="M9 1a8 8 0 1 0 8 8H9z"/><path d="M11 1v6h6"/></svg></span>
    <span class="fab"><svg width="14" height="14" viewBox="0 0 14 14" stroke="#fff" stroke-width="2"><path d="M7 1v12M1 7h12"/></svg></span>
    <span class="nav-slot"><svg width="18" height="18" viewBox="0 0 18 18" fill="none" stroke="#3b3a45" stroke-width="1.6"><circle cx="9" cy="9" r="8"/><circle cx="9" cy="9" r="4.5"/><circle cx="9" cy="9" r="1.5"/></svg></span>
    <span class="nav-slot"><svg width="18" height="18" viewBox="0 0 18 18" fill="none" stroke="#3b3a45" stroke-width="1.6"><rect x="1" y="1" width="6" height="6"/><rect x="11" y="1" width="6" height="6"/><rect x="1" y="11" width="6" height="6"/><rect x="11" y="11" width="6" height="6"/></svg></span>
  </nav>
  <span class="home-bar"></span>
</section>

</body>
</html>
```